High End Notary Service Business Card Design

Want a professional and elegant/luxurious business card that is clean and simple in the design. A notary is a trusted professional that helps people sign very important documents. The card should be in alignment with this service provided.

Most of the time, service will be for the purchase of a home or refinance of a mortgage

There is NO LOGO. This is aesthetic. A look and feel. Conveying professionalism and concierge level of service.

Target Market(s)

Other business professionals, Lawyers, Escrow Officers, Loan Officers

Industry/Entity Type

Legal

Contact Information for Business Card

This will be a one-sided business card

Colors
35a7d7
3176b5
85cae6
d3a5cc
b868aa
ffffff
0356a4

Requirements
Must have
• Lorena T. Mirabel-Hodgkins
Notary Public

642-871-3094
MirabelSigningDesk@Wexmail.com
Nice to have
• Headshot photo below. Convey the aspect of signing documents. No black cards. Preference is shades of blue: light blue, navy, aqua, gold, white, or lavendar, etc.
Should not have
• No scales or legal scales.

```html
<!DOCTYPE html>
<html lang="en">
<head>
<meta charset="utf-8">
<title>Lorena T. Mirabel-Hodgkins — Notary Public</title>
<link rel="stylesheet" href="https://fonts.googleapis.com/css2?family=Cinzel:wght@600&family=Montserrat:wght@500&display=swap">
<style>
  :root {
    --backdrop: #3a3a3a;
    --card: #ffffff;
    --lavender: #a089c3;
    --aqua: #29b1e1;
    --ink: #0c0c0c;
    --on-lavender: #ffffff;
  }
  html, body {
    margin: 0;
    padding: 0;
    width: 1200px;
    height: 913px;
    overflow: hidden;
    background: var(--backdrop);
  }
  .stage {
    position: relative;
    width: 1200px;
    height: 913px;
    box-sizing: border-box;
    border: 1px solid #111;
  }
  .business-card {
    position: absolute;
    left: 165px;
    top: 208px;
    width: 871px;
    height: 497px;
    background: var(--card);
    overflow: hidden;
  }
  .card-art {
    position: absolute;
    inset: 0;
    width: 100%;
    height: 100%;
  }
  .card-art .frame { fill: none; stroke: var(--lavender); stroke-width: 7; }
  .card-art .lavender-wave { fill: var(--lavender); }
  .card-art .aqua-swoosh { fill: var(--aqua); }
  .identity {
    position: absolute;
    left: 0;
    right: 0;
    top: 124px;
    margin: 0;
    text-align: center;
    font-family: "Cinzel", "Trajan Pro", serif;
    font-weight: 600;
    color: var(--ink);
    text-transform: uppercase;
    line-height: 54px;
  }
  .identity .holder-name { display: block; font-size: 43px; letter-spacing: -0.3px; }
  .identity .holder-title { display: block; font-size: 43px; letter-spacing: 2.5px; }
  .contact-list {
    position: absolute;
    left: 447px;
    top: 394px;
    margin: 0;
    padding: 0;
    list-style: none;
    font-family: "Montserrat", Arial, sans-serif;
    font-weight: 500;
    font-size: 19px;
    color: var(--on-lavender);
    white-space: nowrap;
  }
  .contact-list li {
    display: flex;
    align-items: center;
    height: 39px;
  }
  .contact-icon {
    width: 26px;
    height: 26px;
    margin-right: 12px;
    flex: none;
  }
  .contact-icon circle { fill: var(--on-lavender); }
  .contact-icon .glyph { fill: var(--lavender); }
</style>
</head>
<body>
<div class="stage">
  <div class="business-card">
    <svg class="card-art" viewBox="0 0 727 415" preserveAspectRatio="none" aria-hidden="true">
      <rect class="frame" x="17.5" y="17.5" width="691" height="380"/>
      <path class="lavender-wave" d="M0,279 C80,322 170,352 275,349 C410,344 520,280 727,302 L727,415 L0,415 Z"/>
      <path class="aqua-swoosh" d="M160,328 C265,336 385,300 475,262 C548,232 630,222 727,258 L727,287 C630,258 548,266 475,292 C385,322 270,336 160,328 Z"/>
    </svg>

    <h1 class="identity">
      <span class="holder-name">Lorena T. Mirabel-Hodgkins</span>
      <span class="holder-title">Notary Public</span>
    </h1>

    <ul class="contact-list">
      <li class="contact-phone">
        <svg class="contact-icon" viewBox="0 0 24 24" aria-hidden="true">
          <circle cx="12" cy="12" r="12"/>
          <path class="glyph" d="M8.2 5.6c.5-.3 1.1-.2 1.4.3l1.2 2c.3.5.2 1-.2 1.4l-.8.7c.6 1.4 1.7 2.6 3.1 3.3l.8-.8c.4-.4 1-.4 1.4-.1l2 1.2c.5.3.6.9.3 1.4l-.8 1.2c-.4.6-1.2.9-1.9.7-3.6-1-6.5-3.9-7.5-7.5-.2-.7.1-1.5.7-1.9z"/>
        </svg>
        <span>642-871-3094</span>
      </li>
      <li class="contact-email">
        <svg class="contact-icon" viewBox="0 0 24 24" aria-hidden="true">
          <circle cx="12" cy="12" r="12"/>
          <path class="glyph" d="M6 9.5 12 6l6 3.5V17H6z"/>
          <path d="M7.2 10 12 13l4.8-3" fill="none" stroke="#ffffff" stroke-width="1.2"/>
        </svg>
        <span>MirabelSigningDesk@Wexmail.com</span>
      </li>
    </ul>
  </div>
</div>
</body>
</html>
```